Book Cover for nonfiction book about defeating one's grief

I need a book cover (front and back) for a book titled Senderos de Sauces (Willow Paths). I have included a word document of the back cover copy. I liked the design of When the river turns (http://www.pixelvarno.com/design/4817302) so something like that would be nice. But if you have a better idea that's fine.
Target Market(s)
People suffering from the loss of a loved one
Requirements
Must have
- Please move the author information (which is the first paragraph) so that it is the last paragraph
- Please include my middle initial in the name (Derek T. Fenwick)
- 6 x 9 inch book, 9mm spine width, 5cm x 3 cm UPC placeholder on back cover
- Thanks!
Nice to have
- should convey relief from grief or some one grieving

```html
<!DOCTYPE html>
<html lang="es">
<head>
<meta charset="utf-8">
<title>Senderos de Sauces — Cubierta</title>
<link href="https://fonts.googleapis.com/css2?family=Lobster&family=Yellowtail&family=Open+Sans:wght@400&display=swap" rel="stylesheet">
<style>
  :root {
    --paper: #f7e5ad;
    --paper-light: #fbefc8;
    --paper-shade: #efd893;
    --ink: #3a2a16;
    --spine: #c1b17f;
    --ring: #6e5233;
    --sun-1: #fff3a0;
    --sun-2: #f2c21c;
    --sun-3: #d99a08;
    --white: #ffffff;
  }
  html, body { margin: 0; padding: 0; width: 1200px; height: 848px; overflow: hidden; background: var(--paper); }
  .cover {
    position: relative; width: 1200px; height: 848px; overflow: hidden;
    background:
      radial-gradient(ellipse at 30% 40%, var(--paper-light) 0%, transparent 60%),
      radial-gradient(ellipse at 85% 60%, var(--paper-light) 0%, transparent 55%),
      linear-gradient(160deg, var(--paper) 0%, var(--paper-shade) 100%);
    color: var(--ink);
  }
  .back-copy {
    position: absolute; left: 66px; top: 120px; width: 490px;
    font-family: "Yellowtail", cursive; font-size: 15.5px; line-height: 21.6px;
    text-align: justify; text-align-last: center;
  }
  .back-copy p { margin: 0; }
  .back-copy .gap { margin-top: 22px; }
  .back-copy .bio { margin-top: 42px; }
  .divider { text-align: center; letter-spacing: 1px; }
  .barcode-area {
    position: absolute; left: 240px; top: 700px; width: 140px; height: 75px;
    background: var(--white); display: flex; align-items: center; justify-content: center;
    font-family: "Open Sans", sans-serif; font-size: 17px; color: var(--ink);
  }
  .spine {
    position: absolute; left: 575px; top: 0; width: 48px; height: 848px; background: var(--spine);
    display: flex; align-items: center; justify-content: flex-start;
  }
  .spine-text {
    writing-mode: vertical-rl; position: absolute; left: 8px; top: 252px;
    white-space: nowrap; display: flex; align-items: center; gap: 12px;
  }
  .spine-title { font-family: "Lobster", cursive; font-size: 25px; }
  .spine-author { font-family: "Open Sans", sans-serif; font-size: 20px; }
  .title-main {
    position: absolute; left: 623px; width: 577px; text-align: center;
    font-family: "Lobster", cursive; margin: 0; font-weight: 400;
  }
  .title-first { top: 120px; font-size: 136px; line-height: 1; }
  .title-last { top: 555px; font-size: 136px; line-height: 1; left: 660px; }
  .title-link {
    position: absolute; left: 875px; top: 548px; font-family: "Lobster", cursive;
    font-size: 64px; transform: rotate(-10deg);
  }
  .emblem { position: absolute; left: 792px; top: 294px; }
  .author-front {
    position: absolute; left: 623px; width: 577px; top: 752px; text-align: center;
    font-family: "Open Sans", sans-serif; font-size: 26px;
  }
</style>
</head>
<body>
<main class="cover">
  <section class="back-copy">
    <p>Por miles de años, se le ha dicho a la humanidad que el dolor es una parte necesaria de la vida, y que el profundo dolor después del fallecimiento de nuestros seres queridos es esperado y un proceso natural. Derek Fenwick dice enfáticamente que no, ¡no lo es! Puedes, y deberías estar emocionalmente estable y espiritualmente contento después de la muerte de un ser querido.</p>
    <p>La gente a veces pasa meses o años sumidos en el dolor paralizante, lo cual los aparta de muchos esfuerzos fructíferos. El dolor sabotea las vidas felices y productivas. Algunas veces la gente que trata con dolor extremo o pérdidas, se convierten en personas enojadas, abusan de las drogas y alcohol o incluso se quitan sus propias vidas. No debe ser de esta manera. La tristeza, cuando alguien se va de nuestras vidas, es normal. No es necesario el dolor intenso.</p>
    <p>Si crees que el dolor no es para ti – la paz emocional y la felicidad sí lo son.</p>
    <p>Vence tu dolor ahora.</p>
    <p class="divider">------------------------</p>
    <p class="gap">La muerte, como parte de la vida, era una norma en la vida de cualquier persona normal. Ahora es raras veces discutida y solo cuando ocurre una emergencia. Senderos de Sauces es una franca discusión sobre la muerte y morir significa traer paz a los corazones de aquellas personas que están en duelo y esas personas que temen su propia muerte. No es insensible, oscuro y fuerte de leer pero es positivo, reconfortante y espiritualmente tranquilizador.</p>
    <p class="bio">Derek Fenwick se graduó de la Universidad Lakeshore Pines y desde entonces ha vivido en Nueva Jersey trabajando como editor y escritor en el mercado de masas, tecnología y los campos de educación. Él es autor de otros tres libros de los que pueden encontrar más en DerekTfenwick.com</p>
  </section>

  <div class="barcode-area">Barcode Area</div>

  <aside class="spine">
    <div class="spine-text">
      <span class="spine-title">Senderos de Sauces</span>
      <span class="spine-author">Author Name</span>
    </div>
  </aside>

  <h1 class="title-main title-first">Senderos</h1>

  <svg class="emblem" width="266" height="266" viewBox="0 0 266 266" role="img" aria-label="Fotografía: un diente de león sostenido por una mano sobre un fondo dorado y luminoso">
    <defs>
      <radialGradient id="sunlight" cx="45%" cy="35%" r="70%">
        <stop offset="0%" stop-color="var(--sun-1)"/>
        <stop offset="55%" stop-color="var(--sun-2)"/>
        <stop offset="100%" stop-color="var(--sun-3)"/>
      </radialGradient>
    </defs>
    <circle cx="133" cy="133" r="126" fill="url(#sunlight)" stroke="var(--ring)" stroke-width="7"/>
  </svg>

  <span class="title-link">de</span>
  <h2 class="title-main title-last">Sauces</h2>

  <p class="author-front">Author Name</p>
</main>
</body>
</html>
```